Website Development for stormbrookvault.com.au

Build a new Wordpress/Responsive website for stormbrookvault.com.au

Target Market(s)

Compliance Managers, Risk Managers, Information Security and Cyber Security Professionals, Chief Data/Digital Officers, Chief Operating/Financial Officers, Business Continuity Professionals, Disaster Recovery Planners, Small Business Owners, Local/Federal Government entities

Industry/Entity Type

Data Service

Coding

Coded - Design and coding required

Number of Pages Required

5+ page

Font styles to use
Sans Serif

Colors

Designer to choose colors to be used in the design.

Requirements
Must have
• 1. Site Structure: Home Page plus the following chapter-pages for a) Services b) About c) Resources d) Blog e) Contact Us
• 2. Prefer site to built on wordpress and we can purchase a theme if needed (we currently use Kelo4 for other sites)
• 3. Blog needs to be wordpress based
• 4. We will host the site ourselves on our own servers
• 5. Responsive Design
Nice to have
• 1. Livechat capability/interface
• 2. Capability for marketing automation integration (such as pinwhirl, flarevo, quillbranchly etc)
• 3. Capability for CRM integration (Tidewarden)

```html
<!DOCTYPE html>
<html lang="en">
<head>
<meta charset="utf-8">
<title>Stormbrook Vault</title>
<link href="https://fonts.googleapis.com/css2?family=Raleway:wght@400;500;600;700;800&family=Roboto:wght@400;500;700&display=swap" rel="stylesheet">
<style>
:root{
  --red:#e5202b;
  --red-dark:#a3121a;
  --black:#000;
  --ink:#1a1a1a;
  --grey:#555;
  --light:#f2f2f2;
  --white:#fff;
}
*{box-sizing:border-box;margin:0;padding:0}
html,body{width:1200px;height:3297px;overflow:hidden}
body{position:relative;font-family:"Raleway",sans-serif;color:var(--ink);background:var(--white)}
.abs{position:absolute}
.btn{display:inline-block;border:2px solid var(--red);color:var(--ink);background:var(--white);font:700 11px "Roboto",sans-serif;padding:6px 12px;border-radius:3px}
.btn-dark{background:var(--black);color:var(--white);border-color:var(--red)}
p{font-size:12px;line-height:1.55}

/* top strip */
.top-strip{left:0;top:0;width:1200px;height:20px;background:var(--black);color:var(--white);font:500 9px "Roboto",sans-serif;display:flex;align-items:center}
.top-strip .note{position:absolute;left:256px;display:flex;align-items:center;gap:5px}
.top-strip .dot{width:10px;height:10px;border-radius:50%;background:var(--red)}
.top-strip .social{position:absolute;right:290px;display:flex;gap:14px}
.top-strip .social span{width:7px;height:7px;border-radius:50%;background:var(--red)}

/* header */
.site-header{left:0;top:20px;width:1200px;height:68px;background:var(--white)}
.brand{left:248px;top:20px;display:flex;align-items:center;gap:8px;font:800 22px "Raleway",sans-serif;color:var(--red)}
.brand i{width:22px;height:22px;background:var(--red)}
.nav{right:265px;top:22px;display:flex;align-items:center;gap:22px;font:500 11px "Roboto",sans-serif}
.nav .active{color:var(--red)}
.nav .btn{padding:5px 12px}

/* hero */
.hero{left:0;top:88px;width:1200px;height:362px;background:radial-gradient(ellipse at 55% 40%,#1b1b1b,#000 70%)}
.hero h1{position:absolute;left:248px;top:85px;width:260px;color:var(--white);font:700 17px/1.3 "Raleway",sans-serif}
.hero .team{position:absolute;left:248px;top:152px;font:500 25px "Raleway",sans-serif;color:var(--white)}
.hero .team em{font-style:normal;color:var(--red)}
.hero .team b{display:inline-block;width:2px;height:24px;background:var(--white);vertical-align:-4px;margin:0 4px 0 1px}
.hero p{position:absolute;left:248px;top:192px;width:250px;color:var(--white);font-size:11px}
.hero .btn{position:absolute;left:248px;top:244px}
.hero-photo{left:575px;top:88px;width:540px;height:362px;background:linear-gradient(135deg,#d9d4cd 0%,#8d8780 35%,#2a2828 65%,#0a0a0a 100%)}

/* services */
.section-title{position:absolute;width:1200px;text-align:center;color:var(--red);font:700 28px "Raleway",sans-serif}
.section-sub{position:absolute;width:1200px;text-align:center;font:400 11px "Roboto",sans-serif;color:var(--grey)}
.service{position:absolute;top:640px;width:170px;text-align:center}
.service svg{display:block;margin:24px auto 14px}
.service h3{font:700 10px "Roboto",sans-serif;letter-spacing:.5px;margin-bottom:6px}
.service p{font-size:10.5px;line-height:1.45;color:var(--grey);padding:0 14px}
.service.featured{color:var(--white)}
.service.featured p{color:var(--white)}

/* about */
.about{left:0;top:924px;width:1200px;height:544px;background:radial-gradient(ellipse at 85% 40%,#3a0608,#0a0a0a 45%,#000 80%)}
.about-photo{left:143px;top:982px;width:410px;height:354px;border-radius:14px;background:linear-gradient(135deg,#0e2a44,#21638a 35%,#0d1e33 60%,#3a80a0 85%,#0a1a2a)}
.about-badge{left:325px;top:1138px;width:258px;height:232px;background:radial-gradient(circle at 50% 50%,#ff3a3a,#b2121a 45%,#4a0508 90%)}
.about-text{left:615px;top:1028px;width:345px;color:var(--white)}
.about-text h2{font:700 30px "Raleway",sans-serif;margin-bottom:16px}
.about-text p{font-size:11px}
.about-text .lead{color:var(--red);font-size:14px;line-height:1.35;margin:12px 0}
.about-text .btn{margin-top:14px}

/* resources */
.arrow-btn{top:1496px;width:32px;height:32px;border:2px solid var(--ink);border-radius:50%}
.resource{position:absolute;top:1598px;display:flex;gap:16px}
.resource .thumb{width:169px;height:209px;flex:none}
.resource .body{width:152px}
.resource h3{color:var(--red);font:500 17px/1.3 "Raleway",sans-serif;margin-bottom:10px}
.resource p{font-size:11px;color:var(--grey);margin-bottom:12px}

/* blog */
.blog{left:0;top:1886px;width:1200px;height:664px;background:linear-gradient(180deg,#c9c9c9 0%,#777 40%,#111 85%,#000)}
.blog .section-title{color:var(--white);top:38px}
.post{position:absolute;top:2000px;width:272px;height:470px;background:var(--white)}
.post .photo{height:250px}
.post h3{text-align:center;font:700 14px "Raleway",sans-serif;margin:22px 0 14px}
.post p{text-align:center;padding:0 22px;font-size:11px;color:var(--grey)}
.post .btn{position:absolute;left:50%;transform:translateX(-50%);bottom:28px}
.dots{left:586px;top:2498px;display:flex;gap:5px}
.dots span{width:6px;height:6px;border-radius:50%;background:var(--white)}
.dots span.on{background:var(--red)}

/* contact */
.contact{left:0;top:2550px;width:1200px;height:505px;background:linear-gradient(180deg,#fff 0%,#f4f4f4 45%,#d6d6d6 100%)}
.contact-rule{left:590px;top:2636px;width:20px;height:3px;background:var(--ink)}
.field-label{position:absolute;font:700 9px "Roboto",sans-serif}
.field{position:absolute;height:30px;border:1px solid #999;background:var(--white);font:400 10px "Roboto",sans-serif;padding:9px 10px;color:var(--grey)}
.field.textarea{height:128px}
.submit{left:562px;top:2978px;padding:4px 14px}

/* footer */
.site-footer{left:0;top:3055px;width:1200px;height:242px;background:var(--black);color:var(--white)}
.footer-brand{left:248px;top:3110px;display:flex;align-items:center;gap:10px;font:800 28px "Raleway",sans-serif;color:var(--red)}
.footer-brand i{width:30px;height:30px;background:var(--red)}
.copyright{left:248px;top:3222px;font:400 9px "Roboto",sans-serif;color:var(--white)}
.footer-col h4{font:700 20px "Raleway",sans-serif;margin-bottom:22px}
.footer-col li{list-style:none;font:400 10px "Roboto",sans-serif;display:flex;align-items:center;gap:10px;margin-bottom:16px}
.footer-col li span{width:9px;height:9px;background:var(--red);border-radius:50%}
.footer-col .social{display:flex;gap:14px}
.footer-col .social span{width:8px;height:8px;border-radius:50%;background:var(--red)}
</style>
</head>
<body>

<div class="abs top-strip">
  <div class="note"><span class="dot"></span><b>Special for all the users</b> | Lorem Ipsum is simply dummy. <b>Learn More</b></div>
  <div class="social"><span></span><span></span><span></span><span></span></div>
</div>

<header class="abs site-header">
  <div class="abs brand"><i></i>Stormbrook Vault</div>
  <nav class="abs nav">
    <span class="active">Services</span><span>About</span><span>Resources</span><span>Blog</span>
    <span class="btn">Contact Us</span>
  </nav>
</header>

<section class="abs hero">
  <h1>Lorem Ipsum is simply dummy text of the printing and typesetting industry.</h1>
  <div class="team"><em>Stormbrook</em><b></b>Team</div>
  <p>Lorem Ipsum is simply dummy text of the printing and typesetting industry.</p>
  <span class="btn btn-dark">Learn More</span>
</section>
<div class="abs hero-photo" role="img" aria-label="Photo of a business professional at a desk with data service icons"></div>

<h2 class="section-title" style="top:560px">Services</h2>
<p class="section-sub" style="top:600px">Lorem Ipsum is simply dummy text of the printing and typesetting industry.</p>

<svg class="abs" style="left:428px;top:640px" width="174" height="186" viewBox="0 0 174 186">
  <path d="M4 14 L87 2 L170 14 V110 Q170 160 87 184 Q4 160 4 110 Z" fill="var(--red)"/>
</svg>

<div class="service" style="left:242px">
  <svg width="42" height="42" viewBox="0 0 42 42" fill="none" stroke="var(--red)" stroke-width="2.5"><rect x="4" y="4" width="34" height="24"/><path d="M10 22 l8-8 6 5 8-10 M21 28 v8 M12 40 l9-4 9 4"/></svg>
  <h3>BUSINESS PROCESSES</h3><p>Lorem Ipsum is simply dummy text of the printing and typesetting industry.</p>
</div>
<div class="service featured" style="left:430px">
  <svg width="42" height="42" viewBox="0 0 42 42" fill="none" stroke="#fff" stroke-width="2.5"><rect x="4" y="8" width="34" height="12" rx="3"/><rect x="4" y="22" width="34" height="12" rx="3"/><path d="M30 14 h3 M30 28 h3"/></svg>
  <h3>BUSINESS PROCESSES</h3><p>Lorem Ipsum is simply dummy text of the printing and typesetting industry.</p>
</div>
<div class="service" style="left:604px">
  <svg width="42" height="42" viewBox="0 0 42 42" fill="none" stroke="var(--red)" stroke-width="2.5"><path d="M10 26 q-7 0-7-7 q0-7 8-7 q3-8 11-8 q10 0 11 10 q6 1 6 6 q0 6-7 6 M21 18 v18 M15 30 l6 6 6-6"/></svg>
  <h3>BUSINESS PROCESSES</h3><p>Lorem Ipsum is simply dummy text of the printing and typesetting industry.</p>
</div>
<div class="service" style="left:784px">
  <svg width="42" height="42" viewBox="0 0 42 42" fill="none" stroke="var(--red)" stroke-width="2.5"><rect x="4" y="4" width="34" height="24"/><path d="M10 22 l8-8 6 5 8-10 M21 28 v8 M12 40 l9-4 9 4"/></svg>
  <h3>BUSINESS PROCESSES</h3><p>Lorem Ipsum is simply dummy text of the printing and typesetting industry.</p>
</div>

<section class="abs about"></section>
<div class="abs about-photo" role="img" aria-label="Photo of illuminated server racks in a data centre"></div>
<div class="abs about-badge" role="img" aria-label="Red glowing digital circuit graphic"></div>
<div class="abs about-text">
  <h2>About Us</h2>
  <p>Lorem Ipsum is simply dummy text of the printing and typesetting industry.</p>
  <p class="lead">Lorem Ipsum has been the industry's standard dummy text ever since the 1500s, when an unknown printer took a galley of type and scrambled it to make a type specimen book.</p>
  <p>Lorem Ipsum is simply dummy text of the printing and typesetting industry. Lorem Ipsum has been the industry's standard dummy text ever since the 1500s, when an unknown printer took a galley of type and scrambled it to make a type specimen book.</p>
  <span class="btn btn-dark">Read More</span>
</div>

<svg class="abs arrow-btn" style="left:248px" viewBox="0 0 32 32"><path d="M18 10 l-6 6 6 6" fill="none" stroke="var(--ink)" stroke-width="2.5"/></svg>
<h2 class="section-title" style="top:1494px">Resources</h2>
<svg class="abs arrow-btn" style="left:916px" viewBox="0 0 32 32"><path d="M14 10 l6 6 -6 6" fill="none" stroke="var(--ink)" stroke-width="2.5"/></svg>

<div class="resource" style="left:62px">
  <div class="thumb" role="img" aria-label="Photo of hands typing on a keyboard in blue light" style="background:linear-gradient(135deg,#0b1c3a,#2a5ca8 50%,#07122a)"></div>
  <div class="body"><h3>Lorem Ipsum has been the industry's</h3><p>Lorem Ipsum is simply dummy text of the printing and typesetting industry. Lorem Ipsum has been the industry's standard dummy text ever since the when an unknown.</p><span class="btn">Go to Guide</span></div>
</div>
<div class="resource" style="left:433px">
  <div class="thumb" role="img" aria-label="Sketch of a success diagram on paper" style="background:linear-gradient(135deg,#f3f3f3,#c8c8c8 60%,#9a9a9a)"></div>
  <div class="body"><h3>Lorem Ipsum has been the industry's</h3><p>Lorem Ipsum is simply dummy text of the printing and typesetting industry. Lorem Ipsum has been the industry's standard dummy text ever since the when an unknown.</p><span class="btn">Go to Guide</span></div>
</div>
<div class="resource" style="left:800px">
  <div class="thumb" role="img" aria-label="Fingerprint scan graphic on a dark screen" style="background:radial-gradient(circle at 50% 50%,#8aa0b0,#2b3540 55%,#0d1116)"></div>
  <div class="body"><h3>Lorem Ipsum has been the industry's</h3><p>Lorem Ipsum is simply dummy text of the printing and typesetting industry. Lorem Ipsum has been the industry's standard dummy text ever since the when an unknown.</p><span class="btn">Go to Guide</span></div>
</div>

<section class="abs blog" role="img" aria-label="Background photo of business people silhouetted against office windows">
  <h2 class="section-title">Blog</h2>
</section>
<article class="post" style="left:176px">
  <div class="photo" role="img" aria-label="Photo of two colleagues discussing a chart" style="background:linear-gradient(135deg,#cfd8e0,#8ea2b2 50%,#3e4a56)"></div>
  <h3>Simple Blog Post Demo</h3><p>Lorem Ipsum is simply dummy text of the printing and typesetting industry. Lorem Ipsum has been the industry's standard dummy text ever since the 1500s, when an unknown printer took a galley of type and scrambled it to make a type specimen book.</p><span class="btn">Read More</span>
</article>
<article class="post" style="left:464px">
  <div class="photo" role="img" aria-label="Photo of two businessmen reviewing a tablet" style="background:linear-gradient(135deg,#e6e0d6,#8e8a84 50%,#2c2e34)"></div>
  <h3>Simple Blog Post Demo</h3><p>Lorem Ipsum is simply dummy text of the printing and typesetting industry. Lorem Ipsum has been the industry's standard dummy text ever since the 1500s, when an unknown printer took a galley of type and scrambled it to make a type specimen book.</p><span class="btn">Read More</span>
</article>
<article class="post" style="left:754px">
  <div class="photo" role="img" aria-label="Photo of hands protecting a small red figure" style="background:linear-gradient(135deg,#1c2e44,#2e4a68 50%,#0e1a28)"></div>
  <h3>Simple Blog Post Demo</h3><p>Lorem Ipsum is simply dummy text of the printing and typesetting industry. Lorem Ipsum has been the industry's standard dummy text ever since the 1500s, when an unknown printer took a galley of type and scrambled it to make a type specimen book.</p><span class="btn">Read More</span>
</article>
<div class="abs dots"><span></span><span></span><span class="on"></span></div>

<section class="abs contact" role="img" aria-label="Faint background photo of a city skyline"></section>
<h2 class="section-title" style="top:2576px">Contact Us</h2>
<div class="abs contact-rule"></div>
<p class="section-sub" style="top:2648px;font-size:14px;color:var(--ink)">Contact Us Today To Have A Stormbrook Vault Professional Meet With You.</p>

<span class="field-label" style="left:323px;top:2698px">Name</span>
<div class="field" style="left:323px;top:2710px;width:273px">First Name</div>
<span class="field-label" style="left:609px;top:2698px">Email</span>
<div class="field" style="left:609px;top:2710px;width:271px">@</div>
<span class="field-label" style="left:323px;top:2750px">Phone</span>
<div class="field" style="left:323px;top:2762px;width:273px">+00 000 0000</div>
<span class="field-label" style="left:609px;top:2750px">Select One Drop Down</span>
<div class="field" style="left:609px;top:2762px;width:271px">I'm interested in buying a home<span style="position:absolute;right:10px;top:9px">&#9662;</span></div>
<span class="field-label" style="left:323px;top:2814px">Comment Box</span>
<div class="field textarea" style="left:323px;top:2826px;width:557px">Type Your Message Here</div>
<span class="abs btn submit">Submit</span>

<footer class="abs site-footer"></footer>
<div class="abs footer-brand"><i></i>STORMBROOK VAULT</div>
<div class="abs copyright">2019 &copy; Copyright Stormbrook Vault</div>
<div class="abs footer-col" style="left:701px;top:3115px;color:#fff">
  <h4>Get in Touch</h4>
  <ul>
    <li><span></span>14 Harbour Lane, Brookfield 4069</li>
    <li><span></span>07 5550 1942</li>
    <li><span></span>info@stormbrookvault.com.au</li>
  </ul>
  <div class="social"><span></span><span></span><span></span><span></span></div>
</div>
<div class="abs footer-col" style="left:864px;top:3115px;color:#fff">
  <h4>Support</h4>
  <ul>
    <li><span style="width:4px;height:4px"></span>Request a Quote</li>
    <li><span style="width:4px;height:4px"></span>Privacy Policy</li>
  </ul>
</div>

</body>
</html>
```